Corvena Hotel, city center modern minimal hotel operating all year round, on Rhodes island Greece

city, modern ,all year operating hotel

Target Market(s)

tourists, business agents

Industry/Entity Type

tourism

Coding

Coded - Design and coding required

Number of Pages Required

2 page

Requirements
Must have
• room type photos and descriptions, amenities individual listing (graphic), comments sections, map driving location details
Nice to have
• gallery section, modern and minimal design, amenities section, individual room type descriptions, photos and facilities

```html
<!DOCTYPE html>
<html lang="en">
<head>
<meta charset="utf-8">
<title>Corvena Hotel Rhodes</title>
<link href="https://fonts.googleapis.com/css2?family=Playfair+Display:wght@400;700&family=Mulish:wght@400;600;700&display=swap" rel="stylesheet">
<style>
:root{
  --green:#1d5a3c;
  --green-dark:#1c3124;
  --gold:#cfa24a;
  --ink:#222;
  --text:#666;
  --pale:#eef2f1;
  --pale2:#f3f5f7;
  --line:#d7d7d7;
}
*{margin:0;padding:0;box-sizing:border-box}
html,body{width:1200px;height:3827px;overflow:hidden}
body{position:relative;background:#fff;font-family:'Mulish',sans-serif;color:var(--text)}
.abs{position:absolute}
.serif{font-family:'Playfair Display',serif}

/* header */
.site-header{left:0;top:0;width:1200px;height:65px;background:#fff}
.brand{display:flex;align-items:center;gap:10px}
.brand-mark{width:26px;height:26px;background:var(--gold);transform:rotate(45deg)}
.brand-name{font-family:'Playfair Display',serif;font-size:26px;color:var(--green);letter-spacing:1px}
.site-header .brand{position:absolute;left:132px;top:14px}
.nav{position:absolute;top:25px;font-family:'Playfair Display',serif;font-size:11px;color:#333;letter-spacing:.5px}
.btn-book{left:958px;top:17px;width:112px;height:31px;background:var(--gold);color:#fff;font-family:'Playfair Display',serif;font-size:11px;display:flex;align-items:center;justify-content:center;letter-spacing:.5px}

/* hero */
.hero{left:0;top:65px;width:1200px;height:539px;background:linear-gradient(180deg,#8d8e8c 0%,#6f6a62 30%,#506068 60%,#2c4456 100%)}
.hero-kicker{left:0;top:255px;width:1200px;text-align:center;color:#fff;font-family:'Playfair Display',serif;font-size:11px;letter-spacing:.5px}
.hero-title{left:0;top:266px;width:1200px;text-align:center;color:#fff;font-family:'Playfair Display',serif;font-weight:700;font-size:46px}
.search{left:255px;top:357px;width:670px;height:46px;background:rgba(255,255,255,.25);padding:5px 0 5px 20px;display:flex}
.search .field{background:#fff;height:36px;font-size:10px;color:#444;display:flex;align-items:center;padding-left:16px;border-right:1px solid #ddd;position:relative}
.search .cal{position:absolute;right:10px;top:13px;width:9px;height:9px;border:1px solid #888}
.search .go{background:var(--green);color:#fff;width:117px;height:36px;display:flex;align-items:center;justify-content:center;font-size:10px;font-weight:700}

/* section heads */
.kicker{font-family:'Playfair Display',serif;font-size:11px;color:#333;letter-spacing:.3px}
.title{font-family:'Playfair Display',serif;font-weight:400;font-size:34px;color:#222}
.rule{height:1px;background:var(--line);left:0;width:160px}
.rule-accent{width:30px;height:3px;background:var(--gold)}
.body-copy{font-size:12.5px;line-height:20px;color:#555}

.about-visual{left:612px;top:672px;width:458px;height:330px;background:linear-gradient(135deg,#e3d2ae 0%,#6fa3a0 40%,#2f6f82 65%,#d2ad72 100%)}
.btn-more{left:130px;top:953px;width:130px;height:34px;background:var(--green);color:#fff;font-family:'Playfair Display',serif;font-size:11px;display:flex;align-items:center;justify-content:center}
.btn-more-tip{left:250px;top:962px;width:16px;height:16px;background:var(--gold);transform:rotate(45deg)}
.watermark{left:240px;top:965px;font-family:'Playfair Display',serif;font-size:140px;color:transparent;-webkit-text-stroke:1px #ececec;letter-spacing:6px}

/* rooms */
.room{width:300px;height:380px}
.room-head{height:185px;background:#f2f2f2;padding-top:10px;text-align:center;font-family:'Playfair Display',serif;font-weight:700;font-size:16px;color:#222}
.room-photo{position:absolute;left:13px;top:40px;width:274px;height:173px}
.room-desc{position:absolute;left:0;top:225px;width:280px;font-size:11px;line-height:17px;color:#666}
.room-meta{position:absolute;left:0;top:280px;width:286px;height:32px;border-bottom:1px solid #eee;display:flex;align-items:center}
.ic{width:24px;height:24px;border:1px solid #ccc;border-radius:50%;margin-right:17px;display:flex;align-items:center;justify-content:center}
.ic span{width:9px;height:7px;border:1.5px solid #888;border-radius:1px}
.room-meta .count{margin-left:auto;font-size:9px;color:#888}
.room-meta .count b{color:#333}
.price{position:absolute;left:1px;top:330px;width:112px;height:34px;background:var(--green);color:#fff;font-family:'Playfair Display',serif;font-size:11.5px;display:flex;align-items:center;justify-content:center}
.locate{position:absolute;left:119px;top:330px;width:113px;height:34px;border:1px solid #888;color:#333;font-family:'Playfair Display',serif;font-size:11.5px;display:flex;align-items:center;justify-content:center}

/* features */
.features{left:0;top:2040px;width:1200px;height:325px;background:var(--pale)}
.feature{width:240px;text-align:center}
.feature-icon{width:64px;height:64px;margin:0 auto;background:var(--green);transform:rotate(45deg);display:flex;align-items:center;justify-content:center}
.feature-icon svg{transform:rotate(-45deg)}
.feature h3{font-family:'Playfair Display',serif;font-weight:400;font-size:20px;color:#222;margin-top:26px}
.feature p{font-size:11px;line-height:19px;color:#666;width:190px;margin:10px auto 0}
.feature .dot{width:14px;height:14px;background:var(--gold);transform:rotate(45deg);margin:16px auto 0}
.divider{width:1px;background:#dde3e1}

/* gallery */
.gal-side{top:2590px;height:295px}
.gal-main{left:350px;top:2572px;width:500px;height:331px;background:#fff;padding:6px;box-shadow:0 6px 20px rgba(0,0,0,.12)}
.gal-main div{width:100%;height:100%}
.arrow{top:2723px;width:46px;height:30px;background:#fff;display:flex;align-items:center;justify-content:center;font-size:14px;color:#333}

/* testimonials */
.testimonials{left:0;top:2975px;width:1200px;height:470px;background:var(--pale2)}
.quote{width:300px;height:145px;background:#fff;font-size:11px;line-height:17px;color:#666;text-align:center;padding:32px 24px}
.quote-tip{width:20px;height:20px;background:#fff;transform:rotate(45deg)}
.avatar{width:56px;height:56px;border-radius:50%;border:3px solid #fff}
.who{width:300px;text-align:center}
.who b{display:block;font-family:'Playfair Display',serif;font-size:11.5px;color:#222;letter-spacing:1px;font-weight:400}
.who span{font-family:'Playfair Display',serif;font-size:9px;color:#777}

/* footer */
.footer{left:0;top:3445px;width:1200px;height:382px;background:linear-gradient(180deg,#1e3326,#17281e)}
.foot-head{font-family:'Playfair Display',serif;font-weight:400;font-size:17px;color:var(--gold)}
.foot-link{font-size:11px;line-height:14px;color:#fff}
.social{width:28px;height:28px;border-radius:50%;background:var(--gold)}
.cicon{width:28px;height:28px;border:1px solid #fff;border-radius:50%;display:flex;align-items:center;justify-content:center}
.news-input{left:850px;top:3547px;width:220px;height:33px;background:#fff;font-size:10px;color:#333;padding:11px 10px}
.news-btn{left:850px;top:3585px;width:220px;height:33px;background:var(--gold);color:#fff;font-size:10px;font-weight:700;display:flex;align-items:center;justify-content:center}
.copy{left:0;top:3775px;width:1200px;text-align:center;font-size:8.5px;color:#fff}
.copy em{font-style:normal;color:var(--gold)}
</style>
</head>
<body>

<header class="abs site-header">
  <div class="brand"><span class="brand-mark"></span><span class="brand-name">CORVENA</span></div>
  <span class="nav" style="left:543px">HOME</span>
  <span class="nav" style="left:634px">ROOM</span>
  <span class="nav" style="left:725px">GALLERY</span>
  <span class="nav" style="left:834px">CONTACT US</span>
  <div class="abs btn-book">BOOK NOW</div>
</header>

<section class="abs hero" role="img" aria-label="Hotel terrace overlooking a pool at dusk"></section>
<div class="abs hero-kicker">FEW STEPS TO INTERESTING PLACES</div>
<h1 class="abs hero-title">In The Perfect Location</h1>
<div class="abs search">
  <div class="field" style="width:222px">Where?</div>
  <div class="field" style="width:146px">Check In<span class="cal"></span></div>
  <div class="field" style="width:165px">Check Out<span class="cal"></span></div>
  <div class="go">SEARCH</div>
</div>

<!-- about -->
<div class="abs kicker" style="left:130px;top:672px">ABOUT OUR</div>
<h2 class="abs title" style="left:130px;top:683px">Corvena Hotel Rhodes</h2>
<div class="abs rule" style="top:738px"></div>
<p class="abs body-copy" style="left:130px;top:770px;width:465px">Sed ut perspiciatis unde omnis iste natus error sit voluptatem accusantium doloremque laudantium, totam rem aperiam, eaque ipsa quae ab illo inventore veritatis et quasi architecto beatae vitae dicta sunt explicabo. Nemo enim ipsam voluptatem quia voluptas sit aspernatur aut odit aut fugit, sed quia consequuntur magni dolores eos qui ratione voluptatem sequi nesciunt.</p>
<p class="abs body-copy" style="left:130px;top:883px;width:465px">Sed ut perspiciatis unde omnis iste natus error sit voluptatem accusantium doloremque laudantium, totam rem aperiam...</p>
<div class="abs watermark">WELCOME</div>
<div class="abs btn-more">READ MORE</div>
<div class="abs btn-more-tip"></div>
<div class="abs about-visual" role="img" aria-label="Decorative framed view of a coastal village and the sea"></div>

<!-- rooms -->
<div class="abs kicker" style="left:130px;top:1068px">CORVENA HOTEL</div>
<h2 class="abs title" style="left:130px;top:1079px">Our Rooms</h2>
<div class="abs rule" style="top:1133px"></div>
<div class="abs rule-accent" style="left:130px;top:1132px"></div>

<article class="abs room" style="left:130px;top:1163px"><div class="room-head">Apartment For 4 Adults</div><div class="room-photo" role="img" aria-label="Apartment bedroom with city-view windows" style="background:linear-gradient(135deg,#9ea2a1,#cfcac2 50%,#55534f)"></div><p class="room-desc">Situated on the top floor of the hotel, this fully air-conditioned apartment...</p><div class="room-meta"><div class="ic"><span></span></div><div class="ic"><span></span></div><div class="ic"><span></span></div><div class="count">Comments: <b>52</b></div></div><div class="price">Price: € 4.292</div><div class="locate">View Location</div></article>
<article class="abs room" style="left:450px;top:1163px"><div class="room-head">Superior Double Room</div><div class="room-photo" role="img" aria-label="Superior double room with warm wood panels" style="background:linear-gradient(135deg,#5a4632,#c8b79c 55%,#7d6a55)"></div><p class="room-desc">Situated on the top floor of the hotel, this fully air-conditioned apartment...</p><div class="room-meta"><div class="ic"><span></span></div><div class="ic"><span></span></div><div class="ic"><span></span></div><div class="count">Comments: <b>52</b></div></div><div class="price">Price: € 4.292</div><div class="locate">View Location</div></article>
<article class="abs room" style="left:770px;top:1163px"><div class="room-head">Quadruple Room</div><div class="room-photo" role="img" aria-label="Quadruple room with white bed" style="background:linear-gradient(180deg,#8a8681,#d9d5cf 60%,#a59c92)"></div><p class="room-desc">Situated on the top floor of the hotel, this fully air-conditioned apartment...</p><div class="room-meta"><div class="ic"><span></span></div><div class="ic"><span></span></div><div class="ic"><span></span></div><div class="count">Comments: <b>52</b></div></div><div class="price">Price: € 4.292</div><div class="locate">View Location</div></article>

<article class="abs room" style="left:130px;top:1557px"><div class="room-head">Triple Room</div><div class="room-photo" role="img" aria-label="Triple room with patterned rug" style="background:linear-gradient(135deg,#6a5a46,#d8ccb8 50%,#8c7c68)"></div><p class="room-desc">Situated on the top floor of the hotel, this fully air-conditioned apartment...</p><div class="room-meta"><div class="ic"><span></span></div><div class="ic"><span></span></div><div class="ic"><span></span></div><div class="count">Comments: <b>52</b></div></div><div class="price">Price: € 4.292</div><div class="locate">View Location</div></article>
<article class="abs room" style="left:450px;top:1557px"><div class="room-head">Single Room</div><div class="room-photo" role="img" aria-label="Single room with lounge area and curtains" style="background:linear-gradient(135deg,#7a5e48,#e2d8cc 50%,#9c8470)"></div><p class="room-desc">Situated on the top floor of the hotel, this fully air-conditioned apartment...</p><div class="room-meta"><div class="ic"><span></span></div><div class="ic"><span></span></div><div class="ic"><span></span></div><div class="count">Comments: <b>52</b></div></div><div class="price">Price: € 4.292</div><div class="locate">View Location</div></article>
<article class="abs room" style="left:770px;top:1557px"><div class="room-head">Double Room</div><div class="room-photo" role="img" aria-label="Double room with soft wall lighting" style="background:linear-gradient(135deg,#5c4130,#b89878 50%,#6e5240)"></div><p class="room-desc">Situated on the top floor of the hotel, this fully air-conditioned apartment...</p><div class="room-meta"><div class="ic"><span></span></div><div class="ic"><span></span></div><div class="ic"><span></span></div><div class="count">Comments: <b>52</b></div></div><div class="price">Price: € 4.292</div><div class="locate">View Location</div></article>

<!-- features -->
<section class="abs features"></section>
<div class="abs divider" style="left:360px;top:2045px;height:240px"></div>
<div class="abs divider" style="left:600px;top:2060px;height:245px"></div>
<div class="abs divider" style="left:840px;top:2095px;height:250px"></div>
<div class="abs feature" style="left:120px;top:1996px">
  <div class="feature-icon"><svg width="30" height="30" viewBox="0 0 30 30" fill="none" stroke="#fff" stroke-width="1.6"><path d="M15 26s-8-8-8-14a8 8 0 0 1 16 0c0 6-8 14-8 14z"/><circle cx="15" cy="12" r="3"/></svg></div>
  <h3>Location</h3><p>Medieval city is just a few steps away, so are the beautiful beaches of Elli and Psaropoula.</p><div class="dot"></div></div>
<div class="abs feature" style="left:360px;top:2023px">
  <div class="feature-icon"><svg width="30" height="30" viewBox="0 0 30 30" fill="none" stroke="#fff" stroke-width="1.6"><circle cx="12" cy="13" r="7"/><circle cx="12" cy="13" r="3"/><circle cx="21" cy="19" r="5"/><path d="M21 16v3l2 1"/></svg></div>
  <h3>Operation</h3><p>Famous for its friendliness, cleanliness and various amenities found only in higher...</p><div class="dot"></div></div>
<div class="abs feature" style="left:600px;top:2056px">
  <div class="feature-icon"><svg width="30" height="30" viewBox="0 0 30 30" fill="none" stroke="#fff" stroke-width="1.6"><path d="M15 10c-2-4-8-3-7 1 1 3 7 7 7 7s6-4 7-7c1-4-5-5-7-1z"/><path d="M4 20l6 4h10l6-4"/></svg></div>
  <h3>Friendliness</h3><p>The hotel offers its services to both local and international guests either family or business type.</p><div class="dot"></div></div>
<div class="abs feature" style="left:840px;top:2083px">
  <div class="feature-icon"><svg width="30" height="30" viewBox="0 0 30 30" fill="none" stroke="#fff" stroke-width="1.6"><rect x="5" y="12" width="20" height="12"/><circle cx="11" cy="8" r="3"/><circle cx="19" cy="8" r="3"/><path d="M10 17h10"/></svg></div>
  <h3>Amenities</h3><p>The hotel offers most modern amenities, like satellite television set, mini bar, en sure bathroom...</p><div class="dot"></div></div>

<!-- gallery -->
<div class="abs kicker" style="left:130px;top:2434px">GALLERY</div>
<h2 class="abs title" style="left:130px;top:2445px">Discover The Corvena</h2>
<div class="abs rule" style="top:2503px"></div>
<div class="abs rule-accent" style="left:130px;top:2502px"></div>
<p class="abs serif" style="left:130px;top:2513px;font-size:13px;color:#444">Sed ut perspiciatis unde omnis iste natus error sit voluptatem accusantium</p>
<div class="abs gal-side" role="img" aria-label="Guests checking in at the reception desk" style="left:0;width:350px;background:linear-gradient(90deg,#fff 0%,#d8d3cc 35%,#9a9088 100%)"></div>
<div class="abs gal-side" role="img" aria-label="Guest relaxing by the pool" style="left:850px;width:350px;background:linear-gradient(90deg,#cfd7dc 0%,#e9ecee 50%,#fff 100%)"></div>
<div class="abs gal-main"><div role="img" aria-label="Bright minimal lounge with sea-view windows" style="background:linear-gradient(180deg,#c4c8ca 0%,#e6e8e8 50%,#b7bbbd 100%)"></div></div>
<div class="abs arrow" style="left:316px">&#8249;</div>
<div class="abs arrow" style="left:838px">&#8250;</div>

<!-- testimonials -->
<section class="abs testimonials"></section>
<div class="abs kicker" style="left:130px;top:3016px">TESTIMONIALS</div>
<h2 class="abs title" style="left:130px;top:3027px">Our Client Says</h2>
<div class="abs rule" style="top:3083px"></div>
<div class="abs rule-accent" style="left:130px;top:3082px"></div>

<div class="abs quote" style="left:130px;top:3120px">Sed ut perspiciatis unde omnis iste natus error sit voluptatem accusantium doloremque laudantium, totam rem aperiam, eaque ipsa quae ab illo inventore veritatis et quasi architecto beatae</div>
<div class="abs quote" style="left:450px;top:3120px">Sed ut perspiciatis unde omnis iste natus error sit voluptatem accusantium doloremque laudantium, totam rem aperiam, eaque ipsa quae ab illo inventore veritatis et quasi architecto beatae</div>
<div class="abs quote" style="left:770px;top:3120px">Sed ut perspiciatis unde omnis iste natus error sit voluptatem accusantium doloremque laudantium, totam rem aperiam, eaque ipsa quae ab illo inventore veritatis et quasi architecto beatae</div>
<div class="abs quote-tip" style="left:270px;top:3255px"></div>
<div class="abs quote-tip" style="left:590px;top:3255px"></div>
<div class="abs quote-tip" style="left:910px;top:3255px"></div>
<div class="abs avatar" role="img" aria-label="Guest portrait" style="left:252px;top:3298px;background:#8a7a6e"></div>
<div class="abs avatar" role="img" aria-label="Guest portrait" style="left:572px;top:3298px;background:#c9a27e"></div>
<div class="abs avatar" role="img" aria-label="Guest portrait" style="left:892px;top:3298px;background:#b48f6c"></div>
<div class="abs who" style="left:130px;top:3366px"><b>JON FERRIS</b><span>UK, Brighton</span></div>
<div class="abs who" style="left:450px;top:3366px"><b>JON FERRIS</b><span>UK, Brighton</span></div>
<div class="abs who" style="left:770px;top:3366px"><b>JON FERRIS</b><span>UK, Brighton</span></div>

<!-- footer -->
<footer class="abs footer"></footer>
<div class="abs brand" style="left:132px;top:3515px"><span class="brand-mark"></span><span class="brand-name" style="color:#fff">CORVENA</span></div>
<div class="abs social" style="left:131px;top:3592px"></div>
<div class="abs social" style="left:172px;top:3592px"></div>
<div class="abs social" style="left:213px;top:3592px"></div>

<h4 class="abs foot-head" style="left:430px;top:3480px">Quick Links</h4>
<span class="abs foot-link" style="left:430px;top:3518px">Home</span>
<span class="abs foot-link" style="left:430px;top:3545px">Rooms</span>
<span class="abs foot-link" style="left:430px;top:3572px">Gallery</span>
<span class="abs foot-link" style="left:430px;top:3598px">Contact Us</span>

<h4 class="abs foot-head" style="left:590px;top:3480px">Contact Us</h4>
<div class="abs cicon" style="left:590px;top:3515px"><svg width="12" height="14" viewBox="0 0 12 14" fill="none" stroke="#fff" stroke-width="1.4"><path d="M6 13S1 8 1 5a5 5 0 0 1 10 0c0 3-5 8-5 8z"/><circle cx="6" cy="5" r="1.6"/></svg></div>
<span class="abs foot-link" style="left:622px;top:3516px">14 Aigaiou Street, Rhodes<br>851 00</span>
<div class="abs cicon" style="left:590px;top:3570px"><svg width="12" height="12" viewBox="0 0 12 12" fill="none" stroke="#fff" stroke-width="1.4"><path d="M2 1h3l1 3-2 1a7 7 0 0 0 3 3l1-2 3 1v3c-6 0-9-3-9-9z"/></svg></div>
<span class="abs foot-link" style="left:622px;top:3577px">+30 2241 000 555</span>
<div class="abs cicon" style="left:590px;top:3624px"><svg width="12" height="10" viewBox="0 0 12 10" fill="none" stroke="#fff" stroke-width="1.3"><rect x="1" y="1" width="10" height="8"/><path d="M1 1l5 4 5-4"/></svg></div>
<span class="abs foot-link" style="left:622px;top:3631px">info@corvenahotel.example</span>

<h4 class="abs foot-head" style="left:850px;top:3480px">Newsletter</h4>
<div class="abs news-input">Enter Your Email</div>
<div class="abs news-btn">SUBSCRIBE</div>

<div class="abs" style="left:583px;top:3728px;width:34px;height:34px;border-radius:50%;border:2px solid #fff"></div>
<div class="abs copy">COPYRIGHT © 2022 <em>CORVENA CITY HOTEL RHODES</em>. ALL RIGHTS RESERVED.</div>

</body>
</html>
```